Healthy Supplement featuring Moringa products

Need 3 business card options for our reps to order from Cardloom. Our reps will be ordering from Cardloom once we upload them. Attached is our current designs to show what info needs to be on the cards. Our website is www.tkvitality.com
The business cards will be a template for our reps to order from. Most of our reps are Asian & Hispanic. Please look at our website so you can see who we are to get the look and feel what we need.
Target Market(s)
Adults 30 on up. Health oriented people.
Industry/Entity Type
Health And Wellness
Contact Information for Business Card
Name
Title
Phone
Logo
www.tkvitality.com/my/username
Font styles to use
Requirements
Must have
- Please match our website look and colors. A moringa leaf is nice, but am open to something different.
Nice to have
- Healthy looking and warm, not super cold or too modern.
Should not have
- No harsh colors please.

```html
<!DOCTYPE html>
<html lang="en">
<head>
<meta charset="utf-8">
<title>TK Vitality — Business Card</title>
<link rel="stylesheet" href="https://fonts.googleapis.com/css2?family=Open+Sans:wght@400;600&family=Poppins:wght@600&display=swap">
<style>
  :root {
    --stage: #e9e9e9;
    --paper: #ffffff;
    --leaf-deep: #4a8500;
    --leaf-mid: #6aaa10;
    --leaf-soft: #8cc63f;
    --ink: #4a8500;
  }
  html, body {
    margin: 0;
    width: 1200px;
    height: 1200px;
    overflow: hidden;
    background: var(--stage);
  }
  .canvas { position: relative; width: 1200px; height: 1200px; }
  .card {
    position: absolute;
    left: 262px;
    width: 676px;
    height: 439px;
    display: block;
  }
  .card--front { top: 109px; }
  .card--back { top: 628px; }
  .brand-name { font-family: "Open Sans", sans-serif; font-weight: 600; fill: var(--leaf-mid); }
  .web-line { font-family: "Open Sans", sans-serif; font-weight: 600; fill: var(--ink); letter-spacing: 3px; }
  .person-name { font-family: "Open Sans", sans-serif; font-weight: 400; fill: var(--ink); }
  .person-title { font-family: "Poppins", sans-serif; font-weight: 600; fill: var(--leaf-soft); letter-spacing: 3px; }
  .contact-line { font-family: "Open Sans", sans-serif; font-weight: 400; fill: var(--ink); letter-spacing: 3px; }
  .icon-disc { fill: var(--leaf-deep); }
  .icon-line { fill: none; stroke: #ffffff; stroke-width: 2.2; stroke-linecap: round; stroke-linejoin: round; }
</style>
</head>
<body>
<main class="canvas">

  <!-- Front of card -->
  <svg class="card card--front" viewBox="0 0 1088 707" aria-label="Business card front">
    <defs>
      <linearGradient id="front-top-fill" x1="0" y1="0" x2="1" y2="0.3">
        <stop offset="0" stop-color="#6aaa10"/>
        <stop offset="1" stop-color="#4a8500"/>
      </linearGradient>
      <linearGradient id="front-corner-fill" x1="0" y1="1" x2="1" y2="0">
        <stop offset="0" stop-color="#6aaa10"/>
        <stop offset="1" stop-color="#4a8500"/>
      </linearGradient>
    </defs>
    <rect width="1088" height="707" fill="var(--paper)"/>
    <g role="img" aria-label="Decorative green wave band">
      <path d="M0,0 H1088 V95 C720,35 320,130 0,345 Z" fill="url(#front-top-fill)"/>
      <path d="M1088,455 C960,610 800,690 600,707 H1088 Z" fill="url(#front-corner-fill)"/>
    </g>

    <g class="brand">
      <circle cx="378" cy="400" r="40" fill="var(--leaf-soft)"/>
      <text class="brand-name" x="438" y="424" font-size="66">TK Vitality</text>
    </g>
    <text class="web-line" x="512" y="689" font-size="24" text-anchor="middle">www.tkvitality.com</text>
  </svg>

  <!-- Back of card -->
  <svg class="card card--back" viewBox="0 0 1088 707" aria-label="Business card back">
    <defs>
      <linearGradient id="back-band-fill" x1="0" y1="1" x2="1" y2="0">
        <stop offset="0" stop-color="#6aaa10"/>
        <stop offset="0.5" stop-color="#4a8500"/>
        <stop offset="1" stop-color="#4a8500"/>
      </linearGradient>
    </defs>
    <rect width="1088" height="707" fill="var(--paper)"/>
    <g role="img" aria-label="Decorative green wave band">
      <path d="M0,232 C420,240 880,200 1088,90 V250 C820,215 600,255 455,315 C270,430 270,600 370,707 H0 Z" fill="url(#back-band-fill)"/>
    </g>

    <g class="brand">
      <circle cx="70" cy="120" r="32" fill="var(--leaf-soft)"/>
      <text class="brand-name" x="114" y="134" font-size="40">TK Vitality</text>
    </g>

    <text class="person-name" x="394" y="143" font-size="124">Name</text>
    <text class="person-title" x="468" y="196" font-size="54">Title</text>

    <g class="contact">
      <text class="contact-line" x="870" y="372" font-size="22" text-anchor="end">hello@tkvitality.com</text>
      <text class="contact-line" x="868" y="455" font-size="22" text-anchor="end">+99 555 010 2048</text>
      <text class="contact-line" x="875" y="532" font-size="24" text-anchor="end">www.tkvitality.com</text>

      <circle class="icon-disc" cx="954" cy="370" r="29"/>
      <rect class="icon-line" x="940" y="361" width="28" height="18"/>
      <path class="icon-line" d="M940,361 L954,372 L968,361 M940,379 L950,369 M968,379 L958,369"/>

      <circle class="icon-disc" cx="954" cy="443" r="29"/>
      <path d="M958,433 C952,430 946,436 946,446 C946,454 950,458 955,456 L957,450 L953,447 C952,444 953,440 955,438 L959,440 Z" fill="#ffffff"/>

      <circle class="icon-disc" cx="954" cy="521" r="29"/>
      <circle class="icon-line" cx="954" cy="521" r="13"/>
      <ellipse class="icon-line" cx="954" cy="521" rx="6" ry="13"/>
      <path class="icon-line" d="M941,521 L967,521 M943,514 L965,514 M943,528 L965,528"/>
    </g>
  </svg>

</main>
</body>
</html>
```